The Wagon Rolls Yonder is a food truck, talent show, fundraiser event.

The Pellridge Uplift Foundation is hosting a food truck, talent show, fundraiser called The Wagon Rolls Yonder. We need a flyer designed that incorporates a couple of our existing logos. The theme this year is "Summer Kickoff Jam." The event will be held Wednesday, May 23rd from 3-6 pm at the BRAND NEW Morrow Lakeside Amphitheater (R). I've included some of our logos to incorporate into the flyer. This event is geared towards kids K-12.

Target Market(s)

Kids (K-12) and parents

Industry/Entity Type

Non Profit

Colors

Designer to choose colors to be used in the design.

Requirements
Must have
• Incorporate both logos: Truck (prominent), Foundation logo (not as prominent).
Nice to have
• Might need to have some space to add sponsor logos. Not a must.

```html
<!DOCTYPE html>
<html lang="en">
<head>
<meta charset="utf-8">
<title>Summer Kickoff Jam Flyer</title>
<link rel="stylesheet" href="https://fonts.googleapis.com/css2?family=Archivo+Black&family=Luckiest+Guy&family=Montserrat:wght@600&display=swap">
<style>
  :root {
    --teal: #0b4254;
    --yellow: #f3cd3a;
    --white: #ffffff;
    --grey: #8a8a8a;
    --stage: #e6e7e8;
  }
  html, body {
    margin: 0;
    width: 1200px;
    height: 1200px;
    overflow: hidden;
    background: var(--stage);
  }
  .flyer {
    position: absolute;
    left: 180px;
    top: 6px;
    width: 840px;
    height: 1188px;
    background: var(--white);
    overflow: hidden;
    box-shadow: 0 4px 18px rgba(0,0,0,0.18);
  }
  .flyer-shapes {
    position: absolute;
    inset: 0;
  }
  .headline {
    position: absolute;
    left: 330px;
    top: 60px;
    width: 480px;
    text-align: center;
    font-family: "Luckiest Guy", "Archivo Black", sans-serif;
    font-weight: 400;
    line-height: 0.9;
    margin: 0;
  }
  .headline-top {
    display: block;
    color: var(--white);
    font-size: 54px;
  }
  .headline-main {
    display: block;
    color: var(--yellow);
    font-size: 120px;
  }
  .truck-badge {
    position: absolute;
    left: 60px;
    top: 225px;
    width: 220px;
    height: 220px;
    display: flex;
    align-items: center;
    justify-content: center;
    text-align: center;
    font-family: "Archivo Black", sans-serif;
    font-size: 27px;
    line-height: 1.1;
    color: var(--teal);
    padding: 30px;
    box-sizing: border-box;
  }
  .event-details {
    position: absolute;
    right: 40px;
    top: 570px;
    text-align: right;
    font-family: "Archivo Black", sans-serif;
    color: var(--teal);
    line-height: 1;
  }
  .event-day { font-size: 54px; }
  .event-date { font-size: 64px; margin-top: 4px; }
  .event-time {
    font-size: 86px;
    color: var(--yellow);
    -webkit-text-stroke: 5px var(--teal);
    paint-order: stroke fill;
    margin-top: 4px;
  }
  .venue-lead { font-size: 34px; margin-top: 8px; }
  .venue-name {
    position: absolute;
    right: 40px;
    top: 945px;
    font-family: "Archivo Black", sans-serif;
    font-size: 29px;
    color: var(--teal);
    white-space: nowrap;
  }
  .divider {
    position: absolute;
    left: 50px;
    right: 40px;
    top: 997px;
    height: 4px;
    background: var(--yellow);
  }
  .sponsor-label {
    position: absolute;
    left: 110px;
    top: 1070px;
    font-family: "Montserrat", sans-serif;
    font-weight: 600;
    font-size: 28px;
    color: var(--grey);
  }
  .foundation-mark {
    position: absolute;
    left: 430px;
    top: 1060px;
    display: flex;
    align-items: center;
    gap: 12px;
    font-family: "Archivo Black", sans-serif;
    font-size: 20px;
    line-height: 1.1;
    color: var(--teal);
    width: 300px;
  }
  .foundation-dot {
    flex: none;
    width: 40px;
    height: 40px;
    border-radius: 50%;
    background: var(--yellow);
  }
</style>
</head>
<body>
<main class="flyer">
  <svg class="flyer-shapes" width="840" height="1188" viewBox="0 0 840 1188" xmlns="http://www.w3.org/2000/svg">
    <defs>
      <linearGradient id="truckTones" x1="0" y1="0" x2="0" y2="1">
        <stop offset="0" stop-color="#e4e6e8"/>
        <stop offset="0.5" stop-color="#d9dbdd"/>
        <stop offset="0.55" stop-color="#f1c92e"/>
        <stop offset="1" stop-color="#e0b520"/>
      </linearGradient>
      <linearGradient id="crowdTones" x1="0" y1="0" x2="1" y2="1">
        <stop offset="0" stop-color="#8a8f8a"/>
        <stop offset="0.5" stop-color="#c9cdd0"/>
        <stop offset="1" stop-color="#6d7b80"/>
      </linearGradient>
    </defs>
    <path class="band-yellow" fill="var(--yellow)" d="M0,0 H840 V330 C760,420 620,520 420,610 C260,680 120,700 0,720 Z"/>
    <path class="band-teal" fill="var(--teal)" d="M110,0 H800 C790,120 780,240 750,300 C680,420 520,520 330,600 C310,560 300,460 270,360 C230,220 160,100 110,0 Z"/>
    <circle cx="170" cy="335" r="118" fill="var(--teal)"/>
    <circle cx="170" cy="335" r="106" fill="var(--white)"/>
    <circle cx="170" cy="335" r="96" fill="none" stroke="var(--yellow)" stroke-width="5"/>
    <rect x="410" y="250" width="400" height="290" rx="24" fill="url(#truckTones)" role="img" aria-label="Photo of a yellow and silver vintage food truck with a striped awning"/>
    <path fill="var(--yellow)" d="M0,660 C80,600 220,585 330,600 C420,614 460,668 442,736 C424,796 358,808 306,842 C246,884 186,920 108,926 C60,930 20,922 0,914 Z"/>
    <path fill="var(--teal)" d="M0,672 C80,614 218,600 324,614 C408,627 444,674 428,734 C410,788 350,798 300,830 C242,870 184,906 108,912 C62,915 22,908 0,900 Z"/>
    <path fill="url(#crowdTones)" role="img" aria-label="Photo of a child ordering a treat at a food truck window" d="M0,686 C80,630 216,616 320,628 C396,640 428,682 414,732 C398,780 342,788 294,818 C238,856 182,892 108,898 C64,901 24,894 0,886 Z"/>
  </svg>

  <h1 class="headline">
    <span class="headline-top">Summer Kickoff</span>
    <span class="headline-main">Jam</span>
  </h1>

  <div class="truck-badge">The Wagon Rolls Yonder</div>

  <section class="event-details">
    <div class="event-day">Wednesday</div>
    <div class="event-date">23RD MAY</div>
    <div class="event-time">3-6 PM</div>
    <div class="venue-lead">The BRAND</div>
  </section>
  <div class="venue-name">NEW Morrow Lakeside Amphitheater (R)</div>

  <div class="divider"></div>

  <div class="sponsor-label">Sponsored Logo</div>
  <div class="foundation-mark">
    <span class="foundation-dot"></span>
    <span>The Pellridge Uplift Foundation</span>
  </div>
</main>
</body>
</html>
```